Bright Oak Fitness Facility Business Cards

Business Card Design that incorporates the logo and tagline

Target Market(s)

Fitness, People Who Exercise

Contact Information for Business Card

2817 Mossgrove Bend Road
Tavares, Florida 32190
Phone: 352-555-Jump (5867)
www.brightoakfitness.example
info@brightoakfitness.example

Requirements
Must have
• Logo, Address, Website, email and tagline "More Than A Gym". Colors should be red/black/grey/white

```html
<!DOCTYPE html>
<html lang="en">
<head>
<meta charset="utf-8">
<title>Bright Oak Fitness – Business Cards</title>
<link href="https://fonts.googleapis.com/css2?family=Tinos:wght@400;700&display=swap" rel="stylesheet">
<style>
  :root {
    --stage: #51554f;
    --red: #ed1c24;
    --ink: #231f20;
    --paper: #ffffff;
  }
  html, body {
    margin: 0;
    width: 1200px;
    height: 1200px;
    overflow: hidden;
    background: var(--stage);
  }
  .card {
    position: absolute;
    left: 194px;
    width: 812px;
    height: 464px;
    overflow: hidden;
    font-family: "Tinos", "Times New Roman", serif;
  }
  .card--red { top: 110px; background: var(--red); }
  .card--white { top: 626px; background: var(--paper); }
  .card__sweep {
    position: absolute;
    inset: 0;
    width: 100%;
    height: 100%;
  }
  .brand {
    position: absolute;
    left: 646px;
    top: 128px;
    transform: translateX(-50%);
    white-space: nowrap;
    font-weight: 700;
    font-size: 31px;
    letter-spacing: 0.5px;
  }
  .card--red .brand { color: var(--paper); }
  .card--white .brand { color: var(--ink); left: 652px; }
  .contact {
    position: absolute;
    left: 82px;
    top: 242px;
    margin: 0;
    padding: 0;
    list-style: none;
    color: var(--paper);
    font-size: 22px;
  }
  .contact__item {
    display: flex;
    align-items: center;
    height: 36px;
  }
  .contact__icon {
    width: 18px;
    height: 18px;
    margin-right: 16px;
    fill: var(--red);
  }
  .address {
    position: absolute;
    left: 68px;
    top: 366px;
    margin: 0;
    color: var(--paper);
    font-size: 22px;
    white-space: nowrap;
  }
</style>
</head>
<body>

<section class="card card--red">
  <svg class="card__sweep" viewBox="0 0 1015 581" preserveAspectRatio="none" aria-hidden="true">
    <path fill="var(--ink)" d="M60 0 L145 0 C430 100 620 230 684 331 C560 205 330 80 60 0 Z"/>
    <path fill="var(--paper)" d="M0 0 L20 0 C400 130 738 330 738 490 C738 530 728 560 714 581 L0 581 Z"/>
    <path fill="var(--ink)" d="M0 0 C380 150 698 330 698 490 C698 530 688 560 675 581 L0 581 Z"/>
  </svg>
  <div class="brand">Bright Oak Fitness</div>
  <ul class="contact">
    <li class="contact__item">
      <svg class="contact__icon" viewBox="0 0 24 24"><path d="M6.6 10.8c1.4 2.8 3.8 5.1 6.6 6.6l2.2-2.2c.3-.3.7-.4 1-.2 1.1.4 2.3.6 3.6.6.6 0 1 .4 1 1V20c0 .6-.4 1-1 1C10.6 21 3 13.4 3 4c0-.6.4-1 1-1h3.5c.6 0 1 .4 1 1 0 1.3.2 2.5.6 3.6.1.3 0 .7-.2 1l-2.3 2.2z"/></svg>
      352-555-Jump (5867)
    </li>
    <li class="contact__item">
      <svg class="contact__icon" viewBox="0 0 24 24"><path d="M2 5h20v14H2z M3 6l9 7 9-7" stroke="var(--ink)" stroke-width="1.2"/></svg>
      info@brightoakfitness.example
    </li>
    <li class="contact__item">
      <svg class="contact__icon" viewBox="0 0 24 24"><circle cx="12" cy="12" r="10"/><path d="M6 8c2 0 3 1 3 3s2 2 2 4-1 3-1 5M15 4c0 2 1 3 3 3s2 2 3 3" stroke="var(--ink)" stroke-width="1.4" fill="none"/></svg>
      www.brightoakfitness.example
    </li>
  </ul>
  <p class="address">2817 Mossgrove Bend Road, Tavares, Florida 32190</p>
</section>

<section class="card card--white">
  <svg class="card__sweep" viewBox="0 0 1015 581" preserveAspectRatio="none" aria-hidden="true">
    <path fill="var(--ink)" d="M60 0 L145 0 C430 100 620 230 684 331 C560 205 330 80 60 0 Z"/>
    <path fill="var(--red)" d="M0 0 L20 0 C400 130 738 330 738 490 C738 530 728 560 714 581 L0 581 Z"/>
    <path fill="var(--ink)" d="M0 0 C380 150 698 330 698 490 C698 530 688 560 675 581 L0 581 Z"/>
  </svg>
  <div class="brand">Bright Oak Fitness</div>
  <ul class="contact">
    <li class="contact__item">
      <svg class="contact__icon" viewBox="0 0 24 24"><path d="M6.6 10.8c1.4 2.8 3.8 5.1 6.6 6.6l2.2-2.2c.3-.3.7-.4 1-.2 1.1.4 2.3.6 3.6.6.6 0 1 .4 1 1V20c0 .6-.4 1-1 1C10.6 21 3 13.4 3 4c0-.6.4-1 1-1h3.5c.6 0 1 .4 1 1 0 1.3.2 2.5.6 3.6.1.3 0 .7-.2 1l-2.3 2.2z"/></svg>
      352-555-Jump (5867)
    </li>
    <li class="contact__item">
      <svg class="contact__icon" viewBox="0 0 24 24"><path d="M2 5h20v14H2z M3 6l9 7 9-7" stroke="var(--ink)" stroke-width="1.2"/></svg>
      info@brightoakfitness.example
    </li>
    <li class="contact__item">
      <svg class="contact__icon" viewBox="0 0 24 24"><circle cx="12" cy="12" r="10"/><path d="M6 8c2 0 3 1 3 3s2 2 2 4-1 3-1 5M15 4c0 2 1 3 3 3s2 2 3 3" stroke="var(--ink)" stroke-width="1.4" fill="none"/></svg>
      www.brightoakfitness.example
    </li>
  </ul>
  <p class="address">2817 Mossgrove Bend Road, Tavares, Florida 32190</p>
</section>

</body>
</html>
```